Take Out and Catering Menu for Authentic Mexican Food Catering Company

I have an Authentic Mexican Food Catering Company. I need to design a cool takeout menu. I have my logo and information . Need help with the layout and design. It's two sided, color , 5.5 x 8.5"
I have attached the sample menu, but please disregard the style of it as it doesn't sit well with me. Although it's traditional Mexican Food I'd like it to be a little more modern than this. Take the Nopal Rojo card as an example of style, font, etc.
The back side can be similar to the one provided, I think the trick is to keep it simple.

Target Market(s)

Target is mostly families as there are family style meals and catering for private events such as graduations, birthdays, etc.

Industry/Entity Type

Catering

Font styles to use
Sans Serif

Colors
9bcb3c
f04a50

Requirements
Must have
• I'd like it to have the word TACOS vertically and in a lighter tone under the Preordered Box Section (so people know that these boxed dinners are to make tacos)
Nice to have
• Maybe a nice undertone image

```html
<!DOCTYPE html>
<html lang="en">
<head>
<meta charset="utf-8">
<title>Casa Canela – Take Out &amp; Catering Menu</title>
<link rel="stylesheet" href="https://fonts.googleapis.com/css2?family=Varela+Round&family=Nunito+Sans:wght@400;600;700&display=swap">
<style>
:root{
  --green-dark:#2f6a3f;
  --green:#9bcb3c;
  --green-soft:rgba(155,203,60,.55);
  --pink:#e8174f;
  --ink:#1f1f1f;
  --panel:rgba(255,255,255,.78);
  --stage:#ecebe7;
}
*{box-sizing:border-box;margin:0;padding:0}
html,body{width:1200px;height:1200px;overflow:hidden;background:var(--stage)}
body{position:relative;font-family:"Nunito Sans",Arial,sans-serif;color:var(--ink)}
.card{position:absolute;top:213px;width:547px;height:774px;overflow:hidden}
.card--front{left:43px}
.card--back{left:616px}
.card__photo{position:absolute;inset:0}
.card--front .card__photo{background:radial-gradient(ellipse at 45% 30%,#f4f2ea 0%,#e6e3d6 40%,#d8c9a8 70%,#c79a63 100%)}
.card--back .card__photo{background:radial-gradient(ellipse at 50% 40%,#efe9dc 0%,#dccfae 45%,#c9a35a 70%,#a8452f 100%)}
.card__panel{position:absolute;top:18px;bottom:17px;background:var(--panel);border-radius:24px}
.card--front .card__panel{left:41px;right:60px}
.card--back .card__panel{left:18px;right:19px}
.flower{position:absolute;border-radius:50%;background:radial-gradient(circle,rgba(232,23,79,.9) 0%,rgba(232,23,79,.75) 45%,rgba(232,23,79,0) 72%)}
.masthead{position:absolute;height:93px;border:2px solid var(--green-dark);border-radius:14px;background:rgba(255,255,255,.55);text-align:center}
.brand{font-family:"Varela Round",Arial,sans-serif;color:var(--ink);white-space:nowrap}
.masthead .brand{display:block;font-size:34px;margin-top:14px}
.brand-dot{display:inline-block;width:10px;height:10px;border-radius:50%;background:var(--pink);margin-left:6px;vertical-align:middle}
.tagline{display:block;font-size:12px;margin-top:6px}
.vertical-word{position:absolute;font-family:"Varela Round",Arial,sans-serif;color:var(--green-soft);writing-mode:vertical-rl;transform:rotate(180deg);letter-spacing:2px;line-height:1;text-align:center}
.h-section{font-family:"Varela Round",Arial,sans-serif;color:var(--green-dark);font-size:21px;line-height:1}
.h-item{font-family:"Varela Round",Arial,sans-serif;color:var(--pink);font-size:21px;line-height:1}
.col{position:absolute}
.note{font-size:10px;line-height:1.2;color:#444}
.item{margin-top:8px}
.item p{display:flex;justify-content:space-between;align-items:flex-end;font-size:11px;line-height:1.15;margin-top:3px}
.item p span:first-child{max-width:172px}
.list{font-size:11px;line-height:1.3;font-weight:600;margin-top:4px}
.order{font-family:"Varela Round",Arial,sans-serif;color:var(--green-dark);font-size:22px;line-height:.9}
.phone{font-family:"Varela Round",Arial,sans-serif;color:var(--green-dark);font-size:29px;line-height:1}
.web{font-family:"Varela Round",Arial,sans-serif;color:var(--green-dark);font-size:17px;font-weight:700}
.addr{font-size:12px;line-height:1.2;color:var(--green-dark)}
.sig{font-size:22px}
.gf{position:absolute;font-size:10px;line-height:1.1;color:#333}
.bullets{position:absolute;top:179px;width:150px;font-size:10.5px;line-height:1.15}
.bullets li{list-style:none;position:relative;padding-left:14px;margin-bottom:6px}
.bullets svg{position:absolute;left:0;top:1px;width:11px;height:11px}
.cta{color:var(--green-dark);font-weight:700}
.menu-table{position:absolute;left:66px;top:287px;width:420px}
.menu-head{display:grid;grid-template-columns:168px repeat(4,66px);align-items:end;height:30px}
.menu-head span{font-size:9.5px;line-height:1;color:var(--green-dark);text-align:center;text-transform:uppercase}
.menu-head .h-section{text-align:left;font-size:21px;text-transform:none}
.menu-price{display:grid;grid-template-columns:168px repeat(4,66px);font-size:10.5px;font-weight:700;text-align:center;height:17px;align-items:center;border-bottom:1px solid var(--green)}
.menu-row{display:grid;grid-template-columns:168px repeat(4,66px);height:14.75px;align-items:center;font-size:9.6px;border-bottom:1px solid var(--green)}
.menu-row span{white-space:nowrap}
.menu-row svg{justify-self:center;width:10px;height:10px}
.incl{position:absolute;left:333px;top:587px;width:155px;font-size:9.3px;line-height:1.2;color:#333}
</style>
</head>
<body>
<svg width="0" height="0" style="position:absolute" aria-hidden="true">
  <symbol id="tick" viewBox="0 0 12 12"><path d="M1.5 6.5 L4.5 9.5 L10.5 2.5" fill="none" stroke="#2f6a3f" stroke-width="2" stroke-linecap="round" stroke-linejoin="round"/></symbol>
</svg>

<!-- FRONT: take out -->
<section class="card card--front">
  <div class="card__photo" role="img" aria-label="Soft background photo of plated Mexican food"></div>
  <div class="card__panel"></div>
  <div class="flower" style="left:-10px;top:0;width:120px;height:140px" role="img" aria-label="Red flower ornament"></div>
  <div class="flower" style="left:437px;top:347px;width:125px;height:130px" role="img" aria-label="Red flower ornament"></div>
  <div class="flower" style="left:301px;top:655px;width:136px;height:125px" role="img" aria-label="Red flower ornament"></div>

  <header class="masthead" style="left:110px;width:330px;top:42px">
    <span class="brand">Casa Canela<span class="brand-dot"></span></span>
    <span class="tagline">A little taste of Mexico</span>
  </header>

  <div class="vertical-word" style="left:24px;top:155px;width:80px;height:588px;font-size:86px">TACOS</div>
  <div class="vertical-word" style="left:288px;top:391px;width:48px;height:228px;font-size:54px">ORDER</div>

  <div class="col" style="left:72px;top:149px;width:222px">
    <h2 class="h-section">Pre-ordered<br>Specialty Boxes</h2>
    <p class="note">Each dinner makes 8 Tacos<br>Reheat time aprox 10 minutes</p>
    <div class="item"><h3 class="h-item">Chicken Tinga</h3><p><span>Includes Flour Tortillas, Crema, Salsa, Charro Beans and Rice</span><span>$36.00</span></p></div>
    <div class="item"><h3 class="h-item">Roasted Pork<br>Carnitas</h3><p><span>Includes Corn Tortillas, Nopal Rojo, Charro Beans and Rice</span><span>$36.00</span></p></div>
    <div class="item"><h3 class="h-item">Beef Fajitas</h3><p><span>Includes Corn Tortillas, Nopal Rojo, Charro Beans and Rice</span><span>$36.00</span></p></div>
    <div class="item"><h3 class="h-item">Green<br>Chicken Tinga</h3><p><span>Includes Flour Tortillas, Crema, Charro Beans and Rice</span><span>$36.00</span></p></div>
    <div class="item"><h3 class="h-item">Chipotle<br>Garlic Shrimp</h3><p><span>Includes Flour Tortillas, Chipotle Crema, Charro Beans and Rice</span><span>$39.00</span></p></div>
    <div class="item"><h3 class="h-item">Chicken Enchiladas</h3><p><span>Includes Layers of Corn Tortillas, Shredded Chicken, Roasted Corn, Poblano Peppers, Green Enchilada Sauce, Lots of Crema and Melted Cheese, Charro Beans and Rice</span><span>$35.00</span></p></div>
    <div class="item"><h3 class="h-item">Vegetarian<br>Enchiladas</h3><p><span>Includes Layers of Corn Tortillas, Roasted Corn, Poblano Peppers, Green Enchilada Sauce, Lots of Crema and Melted Cheese, Charro Beans and Rice</span><span>$35.00</span></p></div>
  </div>

  <div class="col" style="left:322px;top:149px;width:200px">
    <h2 class="h-section">Available<br>In Store</h2>
    <div class="list">Chicken Tinga Dinner Box<br>Carnitas Dinner Box</div>
    <h2 class="h-section" style="margin-top:8px">Extras/Sides</h2>
    <div class="list">Fresh Salsas<br>Homemade Chips<br>Fresh Guacamole<br>Variety of Tortillas<br>Mexican Crema<br>Assortment of Mexican Cheese<br>Cilantro Mousse<br>Weekly Specials</div>
  </div>

  <div class="col" style="left:319px;top:391px;width:210px">
    <p class="order">Order by<br>phone or<br>online<br>by 2:00pm<br>for same day<br>pick up</p>
    <p class="phone" style="margin-top:10px">555 014-0504</p>
    <p class="web" style="margin-top:12px">www.casacanela.net</p>
    <p class="addr" style="margin-top:4px">118 Elm St. Riverton NJ 07000<br>In Elm St. Corner Wine Shop</p>
    <p class="brand sig" style="margin-top:12px">Casa Canela<span class="brand-dot"></span></p>
  </div>
  <p class="gf" style="left:421px;top:727px">*ALL GF except<br>for flour tortillas</p>
</section>

<!-- BACK: catering -->
<section class="card card--back">
  <div class="card__photo" role="img" aria-label="Soft background photo of bowls of beans and peppers"></div>
  <div class="card__panel"></div>
  <div class="flower" style="left:-6px;top:7px;width:110px;height:135px" role="img" aria-label="Red flower ornament"></div>
  <div class="flower" style="left:464px;top:67px;width:100px;height:145px" role="img" aria-label="Red flower ornament"></div>
  <div class="flower" style="left:356px;top:651px;width:148px;height:125px" role="img" aria-label="Red flower ornament"></div>

  <header class="masthead" style="left:116px;width:330px;top:42px">
    <span class="brand">Casa Canela<span class="brand-dot"></span></span>
    <span class="tagline">A little taste of Mexico</span>
  </header>

  <div class="vertical-word" style="left:26px;top:155px;width:66px;height:588px;font-size:66px">CATERING</div>

  <h2 class="h-section" style="position:absolute;left:64px;top:152px">Catering</h2>
  <ul class="bullets" style="left:48px">
    <li><svg><use href="#tick"/></svg>Create your own gourmet taco bar from our extense menu or choose from one of our 4 pre-designed packages.</li>
    <li class="cta" style="margin-top:8px"><svg><use href="#tick"/></svg>Contact us to start planning your next event!</li>
  </ul>
  <ul class="bullets" style="left:200px">
    <li><svg><use href="#tick"/></svg>Total party planning services available to include beverage selection, rentals, decorations, party favors, etc. to make your event truly authentic and unique!</li>
  </ul>
  <ul class="bullets" style="left:352px">
    <li><svg><use href="#tick"/></svg>Hire the taco cart for a fun twist!</li>
    <li><svg><use href="#tick"/></svg>We will deliver, set up and decorate with a traditional Mexican flair!</li>
    <li><svg><use href="#tick"/></svg>Service staff available upon request.</li>
  </ul>

  <div class="menu-table">
    <div class="menu-head"><h2 class="h-section">Menu</h2><span>Original<br>Taco Bar</span><span>Fiesta<br>Pack</span><span>Amigos<br>Pack</span><span>The Whole<br>Enchilada<br>Pack</span></div>
    <div class="menu-price"><span></span><span>$22.00pp</span><span>$24.00pp</span><span>$26.00pp</span><span>$29.00pp</span></div>
    <div class="menu-row"><span>Homemade Chips</span><svg><use href="#tick"/></svg><svg><use href="#tick"/></svg><svg><use href="#tick"/></svg><svg><use href="#tick"/></svg></div>
    <div class="menu-row"><span>Nopal Rojo and Chipotle Salsa</span><svg><use href="#tick"/></svg><svg><use href="#tick"/></svg><svg><use href="#tick"/></svg><svg><use href="#tick"/></svg></div>
    <div class="menu-row"><span>Chicken Tinga</span><svg><use href="#tick"/></svg><svg><use href="#tick"/></svg><svg><use href="#tick"/></svg><svg><use href="#tick"/></svg></div>
    <div class="menu-row"><span>Pork Carnitas</span><svg><use href="#tick"/></svg><svg><use href="#tick"/></svg><svg><use href="#tick"/></svg><svg><use href="#tick"/></svg></div>
    <div class="menu-row"><span>Charro Beans</span><svg><use href="#tick"/></svg><svg><use href="#tick"/></svg><svg><use href="#tick"/></svg><svg><use href="#tick"/></svg></div>
    <div class="menu-row"><span>Roasted Corn and peppers</span><svg><use href="#tick"/></svg><svg><use href="#tick"/></svg><svg><use href="#tick"/></svg><svg><use href="#tick"/></svg></div>
    <div class="menu-row"><span>Corn and Flour Tortillas</span><svg><use href="#tick"/></svg><svg><use href="#tick"/></svg><svg><use href="#tick"/></svg><svg><use href="#tick"/></svg></div>
    <div class="menu-row"><span>Crema and Cotija Cheese</span><svg><use href="#tick"/></svg><svg><use href="#tick"/></svg><svg><use href="#tick"/></svg><svg><use href="#tick"/></svg></div>
    <div class="menu-row"><span>Appetizer (empanadas or quesadillas)</span><i></i><svg><use href="#tick"/></svg><svg><use href="#tick"/></svg><svg><use href="#tick"/></svg></div>
    <div class="menu-row"><span>Churros</span><i></i><svg><use href="#tick"/></svg><svg><use href="#tick"/></svg><svg><use href="#tick"/></svg></div>
    <div class="menu-row"><span>Guacamole</span><i></i><i></i><svg><use href="#tick"/></svg><svg><use href="#tick"/></svg></div>
    <div class="menu-row"><span>Shaved Steak Fajitas</span><i></i><i></i><svg><use href="#tick"/></svg><svg><use href="#tick"/></svg></div>
    <div class="menu-row"><span>Chipotle Garlic Shrimp</span><i></i><i></i><i></i><svg><use href="#tick"/></svg></div>
    <div class="menu-row"><span>2 Appetizers</span><i></i><i></i><i></i><svg><use href="#tick"/></svg></div>
    <div class="menu-row"><span>Cilantro Lime Rice</span><i></i><i></i><i></i><svg><use href="#tick"/></svg></div>
    <div class="menu-row"><span>Fancy Churros (In chocolate cup with dulce de leche)</span><i></i><i></i><i></i><svg><use href="#tick"/></svg></div>
  </div>

  <div class="col" style="left:64px;top:587px;width:260px">
    <p class="phone">555 014-0504</p>
    <p class="web" style="margin-top:8px">www.casacanela.net</p>
    <p class="web" style="font-size:15px">hola@casacanela.net</p>
    <p class="web" style="font-size:14px">555 019-4692</p>
    <p class="addr" style="font-size:13px;margin-top:2px">118 Elm St. Riverton NJ 07000<br>In Elm St. Corner Wine Shop</p>
    <p class="brand sig" style="margin-top:6px">Casa Canela<span class="brand-dot"></span></p>
  </div>
  <p class="incl">Includes Delivery, Setup and Décor. Serving trays, (pots, baskets and sarape tablecloths upon request) Includes Serving utensils, Plates forks and Napkins.</p>
</section>
</body>
</html>
```